Power Point CI

Creat a Slide Master which we can use and also add new slides with bullets, or other graphic design which we can fill. Power Point Master Format - also amend the graphics on the PPT - especially the project roadmap or profile page. have a look on our website www.brightlantern.io. I would also appreciate other slides which we can use and fill

Target Market(s)

companies - PE, HR Executive

Industry/Entity Type

Executive Search

Font styles to use
Serif
Other font styles liked:
• Calibri or Coast like on our website

Colors
0094D4
00A9DD
6FCCEA
C7EBF8
E9F6FB

Requirements
Must have
• needs to sleek and slim - prefer white and bright elegant Backgrounds
Nice to have
• it should somehow fit to our website and corporate CI
Should not have
• Full green CI

```html
<!DOCTYPE html>
<html lang="en">
<head>
<meta charset="utf-8">
<title>Bright Lantern – Slide Master Overview</title>
<link href="https://fonts.googleapis.com/css2?family=Open+Sans:wght@300;400;600&display=swap" rel="stylesheet">
<style>
  :root{
    --canvas:#f3f4f5;
    --teal-deep:#0a5269;
    --teal:#0c5b72;
    --teal-mid:#1f6a82;
    --teal-band:#2f7690;
    --teal-soft:#6d9fb1;
    --ice:#c7dfe8;
    --ink:#3f4448;
    --ink-soft:#666b70;
    --rule:#d8dcdf;
    --white:#ffffff;
    --photo-dark:#3a3a3a;
    --photo-light:#8c8c8c;
  }
  *{box-sizing:border-box;margin:0;padding:0}
  html,body{width:1036px;height:1200px;overflow:hidden;background:var(--canvas)}
  body{position:relative;font-family:"Open Sans",Calibri,sans-serif;color:var(--ink)}
  .slide{position:absolute;width:501px;height:281px;background:var(--white);overflow:hidden;box-shadow:0 1px 3px rgba(0,0,0,.08)}
  .col-a{left:17px}.col-b{left:518px}
  .row-1{top:16px}.row-2{top:307px}.row-3{top:597px}.row-4{top:887px}

  .page-no{position:absolute;top:24px;right:10px;font-size:4.5px;color:#b8bcc0}
  .footer-url{position:absolute;left:25px;bottom:12px;font-size:4px;color:var(--teal)}
  .footer-brand{position:absolute;right:10px;bottom:18px;font-size:4.4px;letter-spacing:.5px;color:var(--teal-soft);font-weight:400}

  /* title slides */
  .title-slide{background:linear-gradient(135deg,var(--teal) 0%,var(--teal-deep) 55%,var(--teal) 100%)}
  .title-brand{position:absolute;left:176px;top:118px;font-size:27px;line-height:32px;font-weight:300;letter-spacing:2.6px;color:var(--white);white-space:nowrap}
  .title-cities{position:absolute;left:172px;top:242px;font-size:9.5px;color:#e4eef2;font-weight:400}
  .cover-slide{background:var(--teal-mid)}
  .cover-brand{position:absolute;left:24px;top:52px;font-size:11.5px;font-weight:300;letter-spacing:1.6px;color:var(--white)}
  .cover-cities{position:absolute;left:24px;top:248px;font-size:13px;color:var(--white);font-weight:400}

  /* profile */
  .portrait{position:absolute;left:0;top:0;width:190px;height:281px;background:linear-gradient(160deg,var(--photo-light),var(--photo-dark))}
  .profile-body{position:absolute;left:212px;right:25px;top:58px}
  .profile-name{font-size:19px;font-weight:400;color:var(--teal);text-align:center;margin-bottom:13px}
  .profile-body p{font-size:6.8px;line-height:11.4px;color:var(--ink-soft);text-align:justify;margin-bottom:5px}

  /* header band */
  .header-band{position:absolute;left:0;top:0;width:100%;height:119px;background:linear-gradient(100deg,#3b7e96,#2c7189 60%,#4b879c)}
  .header-title{position:absolute;left:0;width:100%;top:16px;text-align:center;font-size:18.5px;font-weight:300;color:var(--white)}
  .page-no.on-band{color:#cfe0e6}

  .work-card{position:absolute;left:25px;top:51px;width:451px;height:198px;background:var(--white);box-shadow:0 1px 5px rgba(0,0,0,.12);padding:6px 8px 0 12px}
  .work-row{display:flex;align-items:center;border-bottom:.6px solid var(--rule);min-height:19.5px;padding:2px 0}
  .work-row:last-child{border-bottom:none}
  .work-row.tall{min-height:38px}
  .work-icon{width:16px;height:14px;flex:none;margin-right:10px}
  .work-text{font-size:7.7px;line-height:10px;color:var(--ink)}
  .work-text b{font-weight:600;color:#222}

  /* values */
  .section-title{position:absolute;left:0;width:100%;top:16px;text-align:center;font-size:18.5px;font-weight:300;color:var(--teal)}
  .value{position:absolute;width:146px}
  .value h3{font-size:6.6px;font-weight:400;color:var(--teal);margin-bottom:6px}
  .value p{font-size:5.8px;line-height:8.8px;color:var(--ink)}
  .values-ring{position:absolute;left:176px;top:84px}

  /* references */
  .ref-card{position:absolute;top:65px;width:217px;height:183px;background:var(--white);box-shadow:0 1px 5px rgba(0,0,0,.12);padding:18px 8px 0 9px}
  .ref-card h3{font-size:8px;font-weight:600;color:var(--teal);padding-bottom:8px;border-bottom:.7px solid var(--teal);letter-spacing:.1px}
  .ref-row{display:flex;justify-content:space-between;border-bottom:.6px solid var(--rule);height:25.3px;padding:5px 18px 0 4px;font-size:6.3px;color:var(--ink)}
  .ref-row span:first-child{padding-top:5px}
  .ref-row:last-child{border-bottom:.7px solid var(--teal)}

  /* target universe */
  .universe{position:absolute;left:0;top:0}
  .desc{position:absolute;width:113px}
  .desc h4{background:var(--teal);color:#e9f2f5;font-size:6.6px;font-weight:400;height:12px;line-height:12px;padding-left:4px}
  .desc ul{list-style:none;margin-top:5px}
  .desc li{font-size:5.6px;color:var(--ink);height:12.4px;padding-left:15px;position:relative}
  .desc li::before{content:"";position:absolute;left:4px;top:3px;width:2px;height:2px;border-radius:50%;background:var(--ink)}
</style>
</head>
<body>

<!-- Title slide -->
<section class="slide title-slide col-a row-1">
  <div class="title-brand">BRIGHT LANTERN</div>
  <div class="title-cities">Hamburg | Wien | Berlin |&nbsp; München</div>
</section>

<!-- Cover slide -->
<section class="slide cover-slide col-b row-1">
  <div class="cover-brand">BRIGHT LANTERN</div>
  <div class="cover-cities">Hamburg | Wien | Berlin |&nbsp; München</div>
</section>

<!-- Profile 1 -->
<section class="slide col-a row-2">
  <div class="portrait" role="img" aria-label="Black and white portrait photo of the founder"></div>
  <span class="page-no">4</span>
  <div class="profile-body">
    <h2 class="profile-name">Dr. Clara Vennhoff-Reiter</h2>
    <p>Clara knows what modern management is all about, and that from many points of view – she has not only successfully appointed many to leadership positions, but she has held those positions herself several times.</p>
    <p>As a graduate of medicine of the Lindenau University Hospital, she first started working for Halvern &amp; Co., where she led the Halvern Hospital Academy. At Ashford Crane Partners, she was responsible for the German healthcare sector. She was a founder and CEO of a healthcare tech start-up, which she successfully sold to an investor. And she was the CHRO of another startup that scaled very fast. To share this comprehensive experience with many companies, she founded Bright Lantern Executive Search in 2021.</p>
    <p>Clara lives in Hamburg with her family.</p>
  </div>
  <span class="footer-brand">BRIGHT LANTERN</span>
</section>

<!-- Profile 2 -->
<section class="slide col-b row-2">
  <div class="portrait" role="img" aria-label="Black and white portrait photo of the co-founder"></div>
  <span class="page-no">5</span>
  <div class="profile-body">
    <h2 class="profile-name">Lena Korbach</h2>
    <p>Lena started her career as a Global Product Manager at Stahlberg in Schaan/Lichtenstein before she spent 3 years in London as the European Sales Manager for Skyward Meridian Airways.</p>
    <p>She then accepted an offer from Ashford Crane Partners (ACP) where she learned the skills of research.</p>
    <p>When her partner was transferred to Bogota in Colombia, she became self-employed (working primarily for ACP), and now, back in Vienna, she founded Bright Lantern Executive Search together with Clara.</p>
    <p>Lena studied International Business Administration at the Danube School of Economics and Business and also graduated from the Global Masters programme. She is mother of 2 children.</p>
  </div>
  <span class="footer-brand">BRIGHT LANTERN</span>
</section>

<!-- Who we are -->
<section class="slide col-a row-3">
  <div class="header-band" role="img" aria-label="Office meeting room photo with teal overlay"></div>
  <h2 class="header-title">Who We Are and How We Work</h2>
  <span class="page-no on-band">6</span>
  <div class="work-card">
    <div class="work-row"><svg class="work-icon" viewBox="0 0 16 14"><circle cx="8" cy="7" r="5" fill="none" stroke="#2f7690" stroke-width=".9"/><circle cx="8" cy="7" r="2" fill="none" stroke="#2f7690" stroke-width=".9"/></svg><p class="work-text"><b>Longstanding experience</b> with a passion for placing (C-Level) Executives in Healthcare and other industries</p></div>
    <div class="work-row tall"><svg class="work-icon" viewBox="0 0 16 14"><circle cx="5" cy="5" r="2" fill="none" stroke="#2f7690" stroke-width=".9"/><circle cx="11" cy="5" r="2" fill="none" stroke="#2f7690" stroke-width=".9"/><circle cx="8" cy="10" r="2" fill="none" stroke="#2f7690" stroke-width=".9"/></svg><p class="work-text">In-depth expertise strong networks in healthcare and , covering all <b>relevant sub-sectors</b> (HC Services, PE Healthcare Rollups, Elderly Care Chains, Physiotherapy, Digital Health, Medical Technology, Healthcare IT), including relevant expertise regarding the regulatory environment in Germany</p></div>
    <div class="work-row"><svg class="work-icon" viewBox="0 0 16 14"><rect x="3" y="2" width="9" height="10" fill="none" stroke="#2f7690" stroke-width=".9"/><line x1="5" y1="5" x2="10" y2="5" stroke="#2f7690" stroke-width=".8"/><line x1="5" y1="8" x2="10" y2="8" stroke="#2f7690" stroke-width=".8"/></svg><p class="work-text">Expertise beyond placement and HR topics, allowing for eye-level discussion around your business</p></div>
    <div class="work-row"><svg class="work-icon" viewBox="0 0 16 14"><circle cx="8" cy="6" r="4" fill="none" stroke="#2f7690" stroke-width=".9"/><line x1="6.5" y1="12" x2="9.5" y2="12" stroke="#2f7690" stroke-width=".9"/></svg><p class="work-text"><b>Creative approaches</b> to finding - and convincing – candidates</p></div>
    <div class="work-row"><svg class="work-icon" viewBox="0 0 16 14"><circle cx="8" cy="7" r="5" fill="none" stroke="#2f7690" stroke-width=".9" stroke-dasharray="2 1"/><circle cx="8" cy="7" r="2" fill="none" stroke="#2f7690" stroke-width=".9"/></svg><p class="work-text"><b>Structured</b> and lean <b>digital search processes</b>, high transparency, comprehensive candidate evaluation</p></div>
    <div class="work-row"><svg class="work-icon" viewBox="0 0 16 14"><circle cx="8" cy="7" r="5" fill="none" stroke="#2f7690" stroke-width=".9" stroke-dasharray="2 1"/><path d="M6 7l1.5 1.5L10 5.5" fill="none" stroke="#2f7690" stroke-width=".9"/></svg><p class="work-text"><b>Referencing</b> of candidates as part of the search process; psychometrics on demand</p></div>
    <div class="work-row"><svg class="work-icon" viewBox="0 0 16 14"><path d="M2 11h5l5-3" fill="none" stroke="#2f7690" stroke-width=".9"/><circle cx="9" cy="4" r="2" fill="none" stroke="#2f7690" stroke-width=".9"/></svg><p class="work-text">Onboarding support to ensure a good start for the candidate</p></div>
    <div class="work-row"><svg class="work-icon" viewBox="0 0 16 14"><circle cx="8" cy="7" r="5" fill="none" stroke="#2f7690" stroke-width=".9"/><path d="M5 7h6" stroke="#2f7690" stroke-width=".9"/></svg><p class="work-text">We work with you <b>personally</b> and act as an <b>ambassador</b> for our clients in the market</p></div>
  </div>
  <span class="footer-brand">BRIGHT LANTERN</span>
  <span class="footer-url">www.brightlantern.io</span>
</section>

<!-- Values -->
<section class="slide col-b row-3">
  <h2 class="section-title">Our Values</h2>
  <span class="page-no">7</span>
  <svg class="values-ring" width="140" height="140" viewBox="0 0 140 140" aria-hidden="true">
    <circle cx="69" cy="69" r="64" fill="none" stroke="#f0f1f2" stroke-width="10"/>
    <circle cx="69" cy="69" r="14" fill="#d6e8ef"/>
  </svg>
  <div class="value" style="left:35px;top:66px"><h3>HONEST</h3><p>We only work with clients who can benefit from our expertise. We are not interested in status symbols, only in achieving results in a way that is transparent and beneficial for everyone.</p></div>
  <div class="value" style="left:328px;top:66px;width:150px"><h3>PRAGMATIC</h3><p>We work fast. But we don’t start until we have a clear goal: We begin by asking “How will you know the appointment was successful, 3 years from now?” This thought drives our process – streamlined, digital, and constantly in communication with you, from the briefing to your new staff member’s first day.</p></div>
  <div class="value" style="left:29px;top:158px;width:148px"><h3>PERSONAL</h3><p>We put all of our resources into finding you the top talents you are looking for – and we get involved ourselves. We have excellent networks, and we are always hot on the heels of fresh talent. That is how we find the people that you need right now. And we help them realise that your company is the right place for them.</p></div>
  <div class="value" style="left:331px;top:168px;width:146px"><h3>DIVERSE</h3><p>We know where the obstacles lie, and we know where things get tough – we have worked through them ourselves, as employees, as managers, as founders, and as mothers. That’s how we know how diversity really works, and how diversity can best benefit your company.</p></div>
  <span class="footer-brand">BRIGHT LANTERN</span>
  <span class="footer-url">www.brightlantern.io</span>
</section>

<!-- References -->
<section class="slide col-a row-4">
  <div class="header-band" role="img" aria-label="Business handshake photo with teal overlay"></div>
  <h2 class="header-title">Relevant reference assignments (excerpt)</h2>
  <span class="page-no on-band">8</span>
  <div class="ref-card" style="left:27px">
    <h3>POSITION TO BE DEFINED</h3>
    <div class="ref-row"><span>Explanation</span><span>Investor/Owner</span></div>
    <div class="ref-row"><span>Explanation</span><span>Investor/Owner</span></div>
    <div class="ref-row"><span>Explanation</span><span>Investor/Owner</span></div>
    <div class="ref-row"><span>Explanation</span><span>Investor/Owner</span></div>
    <div class="ref-row"><span>Explanation</span><span>Investor/Owner</span></div>
  </div>
  <div class="ref-card" style="left:256px">
    <h3>POSITION TO BE DEFINED</h3>
    <div class="ref-row"><span>Explanation</span><span>Investor/Owner</span></div>
    <div class="ref-row"><span>Explanation</span><span>Investor/Owner</span></div>
    <div class="ref-row"><span>Explanation</span><span>Investor/Owner</span></div>
    <div class="ref-row"><span>Explanation</span><span>Investor/Owner</span></div>
    <div class="ref-row"><span>Explanation</span><span>Investor/Owner</span></div>
  </div>
  <span class="footer-brand">BRIGHT LANTERN</span>
  <span class="footer-url">www.brightlantern.io</span>
</section>

<!-- Target universe -->
<section class="slide col-b row-4">
  <h2 class="section-title">Target Universe</h2>
  <span class="page-no">9</span>
  <svg class="universe" width="230" height="281" viewBox="0 0 230 281" font-family="Open Sans, sans-serif" font-size="5.8" fill="#d3e3e9" text-anchor="middle">
    <circle cx="117" cy="152" r="91" fill="#3d7589"/>
    <circle cx="117" cy="166.5" r="75.5" fill="#135a6f"/>
    <circle cx="117" cy="182.5" r="59.5" fill="#1c6980"/>
    <circle cx="117" cy="198.5" r="43.5" fill="#2b7a92"/>
    <circle cx="117" cy="212" r="30" fill="#b9d8e2"/>
    <text x="117" y="73">Insert Your</text><text x="117" y="82">Text Here</text>
    <text x="117" y="103">Insert Your</text><text x="117" y="112">Text Here</text>
    <text x="117" y="134">Insert Your</text><text x="117" y="143">Text Here</text>
    <text x="117" y="166">Insert Your</text><text x="117" y="175">Text Here</text>
  </svg>
  <div class="desc" style="left:234px;top:95px"><h4>Description</h4><ul><li>Donec eu dui eget nisl rhoncus</li><li>At accu dignissimos dublanditiis</li><li>Nemo enim volup voluptas</li></ul></div>
  <div class="desc" style="left:354px;top:95px"><h4>Description</h4><ul><li>Donec eu dui eget nisl rhoncus</li><li>At accu dignissimos dublanditiis</li><li>Nemo enim volup voluptas</li></ul></div>
  <div class="desc" style="left:234px;top:156px"><h4>Description</h4><ul><li>Donec eu dui eget nisl rhoncus</li><li>At accu dignissimos dublanditiis</li><li>Nemo enim volup voluptas</li></ul></div>
  <div class="desc" style="left:354px;top:156px"><h4>Description</h4><ul><li>Donec eu dui eget nisl rhoncus</li><li>At accu dignissimos dublanditiis</li><li>Nemo enim volup voluptas</li></ul></div>
  <span class="footer-brand">BRIGHT LANTERN</span>
  <span class="footer-url">www.brightlantern.io</span>
</section>

</body>
</html>
```